Vidorelt video thumbnail for my simple healthy recipes channel

Hi,

I need a thumbnail that I can re-use for all my videos and only substitute the photo of the recipe/food and maybe the name of the food/recipe if you will include that.

The goal is to attract young people (especially women) that are interested in simple healthy recipes. Please try to use light colors and preferably a shade of #a8d9de and or #debc63 to match my upcoming website.

Here is a Google Drive folder with some materials (photos etc.) to use. There is also a design of my new website so you can match the style.

https://files.brenvoxa.net/share/7Q2ZpLmr4TxWk9HdYs3Ve8Nc1b55?ref=link

Here is my channel: https://www.vidorelt.com/channel/ZRt4bNWqfuYm8GsXaHe902Lp

Thank you,
+Maren

Target Market(s)

Young Women

Industry/Entity Type

Nutritionist

Font styles to use
Other font styles liked:
• Lato preferred but you can be creative

Colors
ffffff

Requirements
Must have
• as above
Nice to have
• as above
Should not have
• as above

```html
<!DOCTYPE html>
<html lang="en">
<head>
<meta charset="utf-8">
<title>Maren Voskel – Channel</title>
<link rel="stylesheet" href="https://fonts.googleapis.com/css2?family=Lato:wght@300;400;700&family=Roboto:wght@400;500&display=swap">
<style>
  :root {
    --page-bg: #f1f1f1;
    --card-bg: #ffffff;
    --ink: #222222;
    --muted: #767676;
    --link: #167ac6;
    --brand-gold: #debc63;
    --brand-blue: #a8d9de;
    --label-ink: #2b2b2b;
    --subscribe: #e62117;
    --white: #ffffff;
  }
  * { box-sizing: border-box; margin: 0; padding: 0; }
  html, body { width: 1200px; height: 534px; overflow: hidden; }
  body { background: var(--page-bg); font-family: "Roboto", Arial, sans-serif; color: var(--ink); }
  .canvas { position: relative; width: 1200px; height: 534px; overflow: hidden; }

  .topbar { position: absolute; left: 0; top: 0; width: 1200px; height: 40px; background: var(--card-bg); }
  .search { position: absolute; left: 0; top: 9px; width: 458px; height: 25px; display: flex; }
  .search-field { flex: 1; border: 1px solid #ccc; border-left: none; background: #fff; }
  .search-button { width: 58px; border: 1px solid #d3d3d3; border-left: none; background: #f8f8f8; display: flex; align-items: center; justify-content: center; }

  .banner { position: absolute; left: 44px; top: 45px; width: 1121px; height: 185px; display: flex; gap: 6px; background: #fff; }
  .banner-strip { flex: 1; height: 100%; }
  .strip-pomegranate { background: linear-gradient(160deg, #b3142a, #6e0a18); }
  .strip-melon { background: linear-gradient(160deg, #f46d4f, #d8402c); }
  .strip-orange { background: linear-gradient(160deg, #ffb22e, #f28a0c); }
  .strip-lemon { background: linear-gradient(160deg, #ffe34a, #f2c300); }
  .strip-kiwi { background: linear-gradient(160deg, #a8d444, #6fa51c); }
  .strip-lettuce { background: linear-gradient(160deg, #7cc843, #3e8d1f); }
  .strip-grape { background: linear-gradient(160deg, #9a4c62, #5a2236); }
  .strip-cherry { background: linear-gradient(160deg, #b5152a, #6a0612); }
  .banner-title { position: absolute; left: 0; right: 0; top: 44px; text-align: center; font-family: "Lato", sans-serif; font-weight: 300; font-size: 92px; line-height: 1; color: var(--white); padding-left: 70px; letter-spacing: 2px; white-space: nowrap; }
  .avatar { position: absolute; left: 58px; top: 45px; width: 89px; height: 89px; background: linear-gradient(180deg, #f3ddc9, #c8a07a); border: 2px solid #fff; }

  .header-card { position: absolute; left: 44px; top: 230px; width: 1121px; height: 72px; background: var(--card-bg); border-bottom: 1px solid #e2e2e2; }
  .channel-name { position: absolute; left: 14px; top: 24px; font-size: 17px; font-weight: 500; }
  .subscribe { position: absolute; right: 15px; top: 25px; display: flex; height: 20px; font-size: 11px; }
  .subscribe-button { background: var(--subscribe); color: #fff; font-weight: 500; display: flex; align-items: center; padding: 0 8px; border-radius: 2px 0 0 2px; }
  .subscribe-count { border: 1px solid #ccc; border-left: none; background: #fafafa; color: #555; padding: 0 5px; display: flex; align-items: center; }

  .uploads-card { position: absolute; left: 44px; top: 310px; width: 1121px; height: 196px; background: var(--card-bg); border-bottom: 1px solid #e2e2e2; }
  .uploads-title { position: absolute; left: 17px; top: 16px; font-size: 14px; font-weight: 500; }
  .video { position: absolute; top: 39px; width: 176px; }
  .video-1 { left: 16px; }
  .video-2 { left: 202px; width: 175px; }
  .video-3 { left: 383px; width: 174px; }
  .thumb { position: relative; height: 99px; display: flex; }
  .thumb-label { width: 87px; display: flex; flex-direction: column; }
  .label-dish { height: 70px; background: var(--brand-gold); padding: 14px 6px 0 9px; font-family: "Lato", sans-serif; font-weight: 700; font-size: 9px; line-height: 12px; text-transform: uppercase; color: var(--label-ink); }
  .label-dish .lead { font-weight: 400; }
  .label-dish .big { font-size: 11px; line-height: 15px; }
  .label-name { flex: 1; background: var(--brand-blue); font-family: "Lato", sans-serif; font-weight: 400; font-size: 10px; color: var(--label-ink); display: flex; align-items: center; justify-content: center; white-space: nowrap; }
  .thumb-photo { flex: 1; }
  .photo-patties { background: linear-gradient(150deg, #e88a4a, #b8532a 60%, #dcd6e6); }
  .photo-salad { background: radial-gradient(circle at 55% 65%, #e0432a 0 30%, #4e8e2e 55%, #2a3a34); }
  .photo-potatoes { background: linear-gradient(150deg, #6e4a22, #d9b35a 55%, #4a6b2a); }
  .video-title { margin-top: 5px; font-size: 12px; font-weight: 500; line-height: 15px; color: var(--link); display: -webkit-box; -webkit-line-clamp: 2; -webkit-box-orient: vertical; overflow: hidden; }
  .video-meta { margin-top: 2px; font-size: 10px; color: var(--muted); white-space: nowrap; }
</style>
</head>
<body>
<div class="canvas">
  <header class="topbar">
    <div class="search">
      <div class="search-field"></div>
      <div class="search-button">
        <svg width="13" height="13" viewBox="0 0 13 13" aria-hidden="true"><circle cx="5" cy="5" r="4" fill="none" stroke="#666" stroke-width="1.6"/><line x1="8" y1="8" x2="12" y2="12" stroke="#666" stroke-width="1.8"/></svg>
      </div>
    </div>
  </header>

  <section class="banner" role="img" aria-label="Row of close-up fruit and vegetable photos: pomegranate, melon, orange, yellow pepper, kiwi, lettuce, grapes, cherries">
    <div class="banner-strip strip-pomegranate"></div>
    <div class="banner-strip strip-melon"></div>
    <div class="banner-strip strip-orange"></div>
    <div class="banner-strip strip-lemon"></div>
    <div class="banner-strip strip-kiwi"></div>
    <div class="banner-strip strip-lettuce"></div>
    <div class="banner-strip strip-grape"></div>
    <div class="banner-strip strip-cherry"></div>
    <div class="banner-title">Maren Voskel</div>
  </section>
  <div class="avatar" role="img" aria-label="Channel profile photo of the host"></div>

  <section class="header-card">
    <h1 class="channel-name">Maren Voskel</h1>
    <div class="subscribe">
      <div class="subscribe-button">Subscribe</div>
      <div class="subscribe-count">26</div>
    </div>
  </section>

  <section class="uploads-card">
    <h2 class="uploads-title">Uploads</h2>

    <article class="video video-1">
      <div class="thumb">
        <div class="thumb-label">
          <div class="label-dish">Vegetable<br>packed<br>salmon<br>patties</div>
          <div class="label-name">Maren Voskel</div>
        </div>
        <div class="thumb-photo photo-patties" role="img" aria-label="Photo of golden salmon patties on a plate"></div>
      </div>
      <p class="video-title">Vegetable Packed Salmon Patties | Simple Healthy Recipes | Maren Voskel</p>
      <p class="video-meta">2,101 views • 7 hours ago</p>
    </article>

    <article class="video video-2">
      <div class="thumb">
        <div class="thumb-label">
          <div class="label-dish"><span class="lead">5 minute</span><br><span class="big">Fish<br>salad</span></div>
          <div class="label-name">Maren Voskel</div>
        </div>
        <div class="thumb-photo photo-salad" role="img" aria-label="Photo of a fresh tomato and green onion salad in a bowl"></div>
      </div>
      <p class="video-title">5 Minute Fresh Salad | Simple Healthy Recipes | Maren Voskel</p>
      <p class="video-meta">10,339 views • 4 days ago</p>
    </article>

    <article class="video video-3">
      <div class="thumb">
        <div class="thumb-label">
          <div class="label-dish">Baked<br>potatoes<br>with<br>mushrooms</div>
          <div class="label-name">Maren Voskel</div>
        </div>
        <div class="thumb-photo photo-potatoes" role="img" aria-label="Photo of baked potatoes with mushrooms and dill"></div>
      </div>
      <p class="video-title">Tasty Baked Potatoes with Mushrooms | Simple Healthy Recipes</p>
      <p class="video-meta">14,623 views • 1 week ago</p>
    </article>
  </section>
</div>
</body>
</html>
```